Design a 4-page brochure for Bramble Peak Fund

Please use the content from the Updated Brochure attachment to design a 4-page 4-color glossy letter sized brochure for Bramble Peak Fund. The content and concept of the brochure are in the attached word document. Additional photos are attached, and a logo for the fund will be forthcoming (the logo is currently a contest on ArtworkHive)
We own the attached photos that can be used in brochure.

Target Market(s)

Investors

Industry/Entity Type

Investment

```html
<!DOCTYPE html>
<html lang="en">
<head>
<meta charset="utf-8">
<title>Bramble Peak Fund II Brochure</title>
<link href="https://fonts.googleapis.com/css2?family=Montserrat:wght@400;500;600;700;800&display=swap" rel="stylesheet">
<style>
  :root {
    --stage: #cfe4e6;
    --paper: #ffffff;
    --blue: #1a8fd8;
    --blue-bright: #2aa6ea;
    --blue-deep: #0b62b5;
    --navy: #0a3f8f;
    --ink: #1565b4;
    --mist: #eef1f4;
    --photo-a: #6b5a52;
    --photo-b: #9fb39a;
    --photo-c: #3a4d6a;
  }
  * { box-sizing: border-box; margin: 0; padding: 0; }
  html, body { width: 1200px; height: 900px; overflow: hidden; }
  body { background: var(--stage); font-family: "Montserrat", Arial, sans-serif; position: relative; }

  .page { position: absolute; width: 560px; height: 420px; background: var(--paper); overflow: hidden; box-shadow: 0 6px 18px rgba(0,40,60,.18); }

  /* Cover */
  .cover { left: 320px; top: 20px; }
  .cover-bands { position: absolute; left: 0; top: 0; width: 560px; height: 420px; }
  .cover-photo { position: absolute; left: 0; top: 78px; width: 560px; height: 190px;
    background: linear-gradient(100deg, var(--photo-a) 0%, #8c8a86 30%, var(--photo-b) 55%, #a7c05a 68%, var(--photo-c) 100%); }
  .cover-headline { position: absolute; right: 30px; top: 284px; text-align: right; color: #fff; font-size: 19px; line-height: 26px; font-weight: 400; }
  .cover-headline span { display: block; white-space: nowrap; }
  .cover-headline .lead { font-weight: 400; font-size: 19px; letter-spacing: .5px; }
  .cover-headline .strong { font-weight: 800; font-size: 21px; letter-spacing: .3px; }
  .cover-headline .tail { font-weight: 400; font-size: 19px; letter-spacing: .5px; }

  /* Spread */
  .spread-left { left: 20px; top: 460px; }
  .spread-right { left: 580px; top: 460px; box-shadow: 6px 6px 18px rgba(0,40,60,.18); }

  .founders { position: absolute; left: 0; top: 0; width: 560px; height: 118px; background: var(--blue-deep);
    color: #fff; font-size: 9.6px; line-height: 1.42; padding: 16px 30px 0 30px; }
  .founders strong { font-weight: 700; }
  .body-copy { position: absolute; left: 30px; top: 132px; width: 500px; color: var(--ink); font-size: 9.9px; line-height: 1.42; }
  .body-copy p { margin-bottom: 8px; text-indent: 14px; }
  .footer-strip { position: absolute; left: 0; bottom: 0; width: 560px; height: 16px; background: var(--blue); }

  .right-bands { position: absolute; left: 0; top: 0; width: 560px; height: 60px; }
  .intro { position: absolute; left: 30px; top: 40px; width: 500px; color: var(--ink); font-size: 9.4px; line-height: 1.38; }
  .proforma { position: absolute; left: 30px; top: 116px; width: 500px; border-collapse: collapse; font-size: 7.2px; color: var(--navy); }
  .proforma td, .proforma th { padding: 1.5px 4px; text-align: center; }
  .proforma .fund-title th { background: var(--navy); color: #fff; font-weight: 700; font-size: 7.6px; letter-spacing: .4px; }
  .proforma .scenario th { background: var(--blue-deep); color: #fff; font-weight: 600; }
  .proforma .cols th { background: var(--blue); color: #fff; font-weight: 600; font-size: 6.6px; }
  .proforma td:first-child { text-align: left; font-weight: 700; }
  .proforma .total td { background: var(--blue-deep); color: #fff; font-weight: 700; }
  .proforma tbody tr:nth-child(even):not(.total) td { background: var(--mist); }
  .note { position: absolute; left: 30px; top: 378px; width: 500px; color: var(--ink); font-size: 7.8px; line-height: 1.35; }
</style>
</head>
<body>

<section class="page cover" aria-label="Front cover">
  <svg class="cover-bands" viewBox="0 0 560 420" aria-hidden="true">
    <polygon points="0,0 560,0 560,30 0,8" fill="var(--navy)"/>
    <polygon points="0,8 560,30 560,82 0,80" fill="var(--blue-bright)"/>
    <polygon points="0,0 260,0 0,40" fill="var(--blue-deep)"/>
    <polygon points="0,262 560,250 560,395 0,375" fill="var(--blue)"/>
    <polygon points="0,262 560,250 560,262 0,282" fill="var(--blue-deep)"/>
    <polygon points="0,375 560,395 560,420 0,420" fill="var(--mist)"/>
  </svg>
  <div class="cover-photo" role="img" aria-label="Photograph of the three fund managers in business suits talking in an office"></div>
  <h1 class="cover-headline">
    <span class="lead">NOW YOU CAN FINALLY</span>
    <span class="strong">EARN SUBSTANTIAL MONTHLY RETURNS</span>
    <span class="tail">WHILE REALIZING SOLID CAPITAL GROWTH</span>
  </h1>
</section>

<section class="page spread-left" aria-label="Inside left page">
  <div class="founders">
    <strong>Messrs. Harlow, Keane</strong> and <strong>Ostrand</strong> founded the Bramble Peak fund family in 2010. Their debut fund was a boutique venture capital fund with investments in a select portfolio of early stage companies. The fund introduced a proprietary structure that gave private equity investors a clear balance of risk and return. In addition to its portfolio companies, the fund was able to add value through its unique structure by creating a holding company for patents filed on its structure, which inures to the benefit of its investors.
  </div>
  <div class="body-copy">
    <p>Bramble Peak is building upon the success of its first fund with the launch of Bramble Peak Fund II (the “Fund”), a venture debt fund registered as a Colorado limited liability company that invests in early to mid-stage companies as well as securities with preferential returns backed by investments in start up companies.</p>
    <p>Fund II pays its investors a 9% annualized cash-on-cash return on a monthly basis, and a preferential return of 1.25x on maturities of 3 years or less. If the Fund extends the maturity of an investment beyond 3 years, the annual return is increased to 12% (beginning in year 4) payable monthly, and the preferential return is increased to 1.5x. The fund is obligated to liquidate the securities it holds to repay investors within five years of the date of their investment.</p>
    <p>The cash flow of the Fund will be derived from the sale or maturity of the fund’s investments and securities. The Pro Forma herein projects the distribution of cash flows to the Fund’s investors. Management receives the excess cash flow of the Fund after the Fund’s obligations to its investors have been satisfied.</p>
    <p>The minimum investment in Fund II is fifty thousand dollars ($50,000). The first three years of interest is paid from a reserve fund and liquidations within the fund’s portfolio pay the preferential returns and any remaining interest payments. This strategy allows the Fund to provide the Fund’s investors with ongoing monthly returns and liquidation preferences upon exit.</p>
  </div>
  <div class="footer-strip"></div>
</section>

<section class="page spread-right" aria-label="Inside right page">
  <svg class="right-bands" viewBox="0 0 560 60" aria-hidden="true">
    <polygon points="360,0 560,0 560,40" fill="var(--blue)"/>
    <polygon points="450,0 560,0 560,20" fill="var(--blue-deep)"/>
  </svg>
  <p class="intro">The targeted portfolio companies are technology companies, and the exit strategy for each company is the sale or licensing of their technology to top companies in their respective industries. It is notable that the sale of any one of the Fund’s portfolio companies could repay the preferential returns before the 3-year maturity date (See Pro Forma), and such payment of the preferential return would terminate the Fund’s obligation to make any additional interest payments.</p>

  <table class="proforma">
    <tr class="fund-title"><th colspan="8">BRAMBLE PEAK FUND II</th></tr>
    <tbody>
      <tr class="scenario"><th colspan="8">1. Exit in 2 Years</th></tr>
      <tr class="cols"><th></th><th>Investment Amount</th><th>Interest Rate</th><th>Interest Received</th><th>Preference Rate</th><th>Preference Amount</th><th>Total Return</th><th>Return on Investment</th></tr>
      <tr><td>YEAR 1</td><td>$100,000</td><td>9%</td><td>$9,000</td><td></td><td></td><td></td><td></td></tr>
      <tr><td>YEAR 2</td><td></td><td>9%</td><td>$9,000</td><td>1.25</td><td>$125,000</td><td></td><td></td></tr>
      <tr class="total"><td>TOTAL:</td><td></td><td></td><td>$18,000</td><td></td><td>$125,000</td><td>$143,000</td><td>43%</td></tr>
    </tbody>
    <tbody>
      <tr class="scenario"><th colspan="8">2. Exit in 3 Years</th></tr>
      <tr class="cols"><th></th><th>Investment Amount</th><th>Interest Rate</th><th>Interest Received</th><th>Preference Rate</th><th>Preference Amount</th><th>Total Return</th><th>Return on Investment</th></tr>
      <tr><td>YEAR 1</td><td>$100,000</td><td>9%</td><td>$9,000</td><td></td><td></td><td></td><td></td></tr>
      <tr><td>YEAR 2</td><td></td><td>9%</td><td>$9,000</td><td></td><td></td><td></td><td></td></tr>
      <tr><td>YEAR 3</td><td></td><td>9%</td><td>$9,000</td><td>1.25</td><td>$125,000</td><td></td><td></td></tr>
      <tr class="total"><td>TOTAL:</td><td></td><td></td><td>$27,000</td><td></td><td>$125,000</td><td>$152,000</td><td>52%</td></tr>
    </tbody>
    <tbody>
      <tr class="scenario"><th colspan="8">3. Exit in 4 Years</th></tr>
      <tr class="cols"><th></th><th>Investment Amount</th><th>Interest Rate</th><th>Interest Received</th><th>Preference Rate</th><th>Preference Amount</th><th>Total Return</th><th>Return on Investment</th></tr>
      <tr><td>YEAR 1</td><td>$100,000</td><td>9%</td><td>$9,000</td><td></td><td></td><td></td><td></td></tr>
      <tr><td>YEAR 2</td><td></td><td>9%</td><td>$9,000</td><td></td><td></td><td></td><td></td></tr>
      <tr><td>YEAR 3</td><td></td><td>9%</td><td>$9,000</td><td></td><td></td><td></td><td></td></tr>
      <tr><td>YEAR 4</td><td></td><td>12%</td><td>$12,000</td><td>1.5</td><td>$150,000</td><td></td><td></td></tr>
      <tr class="total"><td>TOTAL:</td><td></td><td></td><td>$39,000</td><td></td><td>$150,000</td><td>$189,000</td><td>89%</td></tr>
    </tbody>
  </table>

  <p class="note">Please note that these are forward-looking statements by the Fund’s management, which cannot be relied upon to accurately project actual future returns on an investment in the Fund (See Risk Factors in the Fund’s PPM).</p>
  <div class="footer-strip"></div>
</section>

</body>
</html>
```